Vexora Summit 2018 conference Branding banner design

We require branding for our conference Vexora Summit 2018. We need a banner to upload to our registration site, added to the headers of the sponsorship prospectus and print on pull up banners at the conference. The Vexora Summit 2018 conference is a first of its kind. The branding needs to be unique and stand out amongst normal 3D printing conferences. This project will be the highlight of the conference and will be used for all advertising material. It needs to be professional, eye catching, modern and innovative.

Target Market(s)

People who are interested in 3D printing in medicine. There is also a public session, so the banner needs to attract the public.

Industry/Entity Type

Medical And Science

Font styles to use
Sans Serif

Colors
0455a3
e34197
ffffff

Requirements
Must have
• KelvionLab logo
• Unique design related to the conference
• Conference title
Nice to have
• Kelvion Lab colours
Should not have
• No finzo pictures

```html
<!DOCTYPE html>
<html lang="en">
<head>
<meta charset="utf-8">
<title>Vexora Summit 2018 – Banner Concept</title>
<link rel="stylesheet" href="https://fonts.googleapis.com/css2?family=Arimo:wght@400;700&family=Oswald:wght@600;700&display=swap">
<style>
  :root {
    --navy: #2a2a86;
    --pink: #e8337f;
    --hot-pink: #ff3f97;
    --blue: #0a8cf5;
    --deep-blue: #0455a3;
    --white: #ffffff;
    --steel-light: #e2e3e5;
    --steel-mid: #c9cacd;
    --note-ink: #6f6f70;
    --rule: #666666;
    --footer: #2b2b2b;
  }
  * { box-sizing: border-box; margin: 0; padding: 0; }
  html, body { width: 1200px; height: 1200px; overflow: hidden; }
  body {
    position: relative;
    background: linear-gradient(180deg, var(--steel-light) 0%, var(--steel-mid) 50%, var(--steel-light) 100%);
    font-family: "Arimo", Arial, sans-serif;
  }
  .banner {
    position: absolute; left: 64px; top: 106px; width: 1072px; height: 376px;
    display: flex; overflow: hidden;
  }
  .banner__brand {
    width: 352px; height: 100%; background: var(--white);
    position: relative;
  }
  .brand-mark {
    position: absolute; left: 100px; top: 42px; width: 152px; height: 152px;
    border: 10px solid var(--navy); border-radius: 50%;
    display: flex; align-items: center; justify-content: center;
    font-family: "Oswald", sans-serif; font-weight: 700; font-size: 30px; color: var(--navy);
  }
  .conference-title {
    position: absolute; left: 0; right: 0; top: 213px;
    text-align: center;
    font-family: "Oswald", sans-serif; font-weight: 700; color: var(--navy);
    font-size: 50px; line-height: 70px; letter-spacing: -0.5px;
  }
  .conference-title .accent { color: var(--pink); }
  .banner__feature {
    flex: 1; position: relative;
    background: linear-gradient(90deg, var(--pink) 0%, var(--hot-pink) 6%, #7b7ee0 32%, var(--blue) 55%, #0a84ee 80%, var(--deep-blue) 100%);
  }
  .capsule {
    position: absolute; left: 64px; top: 66px; width: 592px; height: 250px;
    border: 6px solid var(--white); border-radius: 125px; overflow: hidden;
    background: linear-gradient(90deg, rgba(255,200,225,0.85) 0%, rgba(220,190,235,0.75) 35%, rgba(170,200,250,0.8) 62%, transparent 62%);
  }
  .capsule__scene {
    position: absolute; left: 296px; top: 4px; right: 4px; bottom: 4px;
    border-left: 6px solid var(--white);
    border-radius: 0 118px 118px 0;
    background: linear-gradient(160deg, #9fd3ff 0%, #2f8ef0 40%, #0c5fd6 75%, #1a4fb8 100%);
  }
  .capsule__tagline {
    position: absolute; left: 64px; top: 14px;
    font-family: "Oswald", sans-serif; font-weight: 600; font-size: 20px; line-height: 26px;
    color: #1565e0;
  }
  .capsule__tagline span { display: block; }
  .capsule__tagline span + span { padding-left: 40px; }
  .wordmark {
    position: absolute; font-family: "Arimo", Arial, sans-serif; font-weight: 700; color: var(--white);
    text-shadow: 2px 3px 0 #c9c2d2, 4px 6px 6px rgba(0,0,0,0.35);
    line-height: 1; white-space: nowrap;
  }
  .wordmark--3d { left: 216px; top: 73px; font-size: 128px; letter-spacing: -6px; }
  .wordmark--p { left: 78px; top: 150px; font-size: 165px; transform: rotate(-12deg); transform-origin: 30% 85%; }
  .wordmark--rint { left: 164px; top: 182px; font-size: 128px; letter-spacing: -5px; }
  .rule { position: absolute; width: 3px; background: var(--rule); }
  .note {
    position: absolute; color: var(--note-ink);
    font-size: 46px; line-height: 46px; white-space: nowrap;
    text-shadow: 1px 1px 0 rgba(255,255,255,0.8), -1px -1px 0 rgba(0,0,0,0.25);
  }
  .note--brand { left: 84px; top: 665px; }
  .note--type { left: 565px; top: 557px; }
  .note--capsule { left: 498px; top: 825px; }
  .footer { position: absolute; left: 0; right: 0; top: 1102px; bottom: 0; background: var(--footer); }
</style>
</head>
<body>
  <section class="banner">
    <div class="banner__brand">
      <div class="brand-mark">Vexora</div>
      <h1 class="conference-title"><span class="accent">Vexora</span> Summit<br>2018</h1>
    </div>
    <div class="banner__feature">
      <div class="capsule">
        <div class="capsule__scene" role="img" aria-label="Blue-tinted photo of glass skyscrapers seen from below">
          <p class="capsule__tagline"><span>Print Our</span><span>New Life</span></p>
        </div>
      </div>
      <span class="wordmark wordmark--3d">3D</span>
      <span class="wordmark wordmark--p">P</span>
      <span class="wordmark wordmark--rint">rint</span>
    </div>
  </section>

  <div class="rule" style="left:64px; top:500px; height:236px;"></div>
  <div class="rule" style="left:477px; top:496px; height:412px;"></div>
  <div class="rule" style="left:546px; top:496px; height:140px;"></div>

  <p class="note note--brand">Vexora repeats<br>in logo and<br>title, therefore<br>simplified.</p>
  <p class="note note--type">3D design of fonts<br>emphasizes the 3D theme.<br>Rotated P adds<br>playfulness and vitality.</p>
  <p class="note note--capsule">Capsule implies medicine,<br>and the invitation to ‘Print Our<br>New Life’ welcomes public that<br>just interested in 3D printing.</p>

  <footer class="footer"></footer>
</body>
</html>
```